Business Card Design needed for logo design project

Would like a professional business card for a company involved in financial and latest technologies including CAD design. We would like the card to convey professionalism and communicate that we are involved in up to date technology solutions.

Target Market(s)

Business 2 Business sales

Industry/Entity Type

Financial

Colors

Designer to choose colors to be used in the design.

Requirements
Must have
• Business Name
Logo
Name
Phone
Email
Nice to have
• Website

```html
<!DOCTYPE html>
<html lang="en">
<head>
<meta charset="utf-8">
<title>QUORVA Business Card</title>
<link rel="stylesheet" href="https://fonts.googleapis.com/css2?family=Montserrat:wght@800&family=Open+Sans:wght@400&family=Roboto+Slab:wght@400;700&display=swap">
<style>
  :root {
    --brand-red: #d4313a;
    --brand-navy: #1f2a4d;
    --paper: #ffffff;
    --ink: #4a4a4a;
    --ink-soft: #6a6a6a;
    --backdrop: #e4e4e4;
  }
  * { margin: 0; padding: 0; box-sizing: border-box; }
  html, body { width: 1200px; height: 800px; overflow: hidden; }
  body {
    background: var(--backdrop);
    display: flex;
    align-items: center;
    justify-content: center;
    gap: 60px;
  }
  .card {
    position: relative;
    width: 525px;
    height: 300px;
    box-shadow: 0 8px 24px rgba(0,0,0,0.18);
    overflow: hidden;
  }
  .wordmark {
    font-family: 'Montserrat', sans-serif;
    font-weight: 800;
    letter-spacing: 1px;
    line-height: 1;
  }

  /* Front */
  .card-front { background: var(--brand-red); }
  .card-front .wordmark {
    position: absolute;
    top: 108px;
    left: 0; right: 0;
    text-align: center;
    font-size: 44px;
    color: var(--paper);
  }
  .card-front .website {
    position: absolute;
    bottom: 30px;
    left: 0; right: 0;
    text-align: center;
    font-family: 'Open Sans', sans-serif;
    font-size: 19px;
    color: var(--paper);
    letter-spacing: 0.5px;
  }

  /* Back */
  .card-back { background: var(--paper); }
  .flag-band {
    position: absolute;
    top: 0; left: 0;
    width: 26px;
    height: 112px;
    background: linear-gradient(160deg, var(--brand-navy) 0%, #3b4670 50%, var(--brand-red) 100%);
  }
  .side-strip {
    position: absolute;
    top: 112px; bottom: 0; left: 0;
    width: 26px;
    background: var(--brand-red);
    display: flex;
    flex-direction: column;
    align-items: center;
    padding-top: 24px;
    gap: 9px;
  }
  .side-strip svg { width: 12px; height: 12px; display: block; }
  .card-back .wordmark {
    position: absolute;
    top: 36px;
    right: 62px;
    font-size: 30px;
    color: var(--brand-red);
  }
  .owner {
    position: absolute;
    top: 138px;
    right: 40px;
    text-align: right;
    font-family: 'Roboto Slab', serif;
    color: var(--ink);
  }
  .owner-name { font-size: 19px; font-weight: 700; }
  .owner-title { font-size: 8px; margin-top: 3px; color: var(--ink); }
  .contact-list {
    position: absolute;
    top: 130px;
    left: 42px;
    list-style: none;
    font-family: 'Open Sans', sans-serif;
    font-size: 13px;
    color: var(--ink-soft);
    line-height: 21px;
  }
</style>
</head>
<body>

  <section class="card card-front" aria-label="Business card front">
    <div class="wordmark">QUORVA</div>
    <div class="website">www.nameofcompany.com</div>
  </section>

  <section class="card card-back" aria-label="Business card back">
    <div class="flag-band" role="img" aria-label="National flag band motif"></div>
    <div class="side-strip">
      <svg viewBox="0 0 12 12" aria-label="Website"><circle cx="6" cy="6" r="5" fill="none" stroke="#fff" stroke-width="1.3"/><line x1="1" y1="6" x2="11" y2="6" stroke="#fff" stroke-width="1"/><ellipse cx="6" cy="6" rx="2.2" ry="5" fill="none" stroke="#fff" stroke-width="1"/></svg>
      <svg viewBox="0 0 12 12" aria-label="Phone"><rect x="3" y="1" width="6" height="10" rx="1.2" fill="none" stroke="#fff" stroke-width="1.3"/><circle cx="6" cy="9" r="0.7" fill="#fff"/></svg>
      <svg viewBox="0 0 12 12" aria-label="Email"><rect x="1" y="2.5" width="10" height="7" fill="none" stroke="#fff" stroke-width="1.2"/><polyline points="1,2.5 6,7 11,2.5" fill="none" stroke="#fff" stroke-width="1.2"/></svg>
      <svg viewBox="0 0 12 12" aria-label="Messaging"><circle cx="6" cy="6" r="5" fill="#fff"/></svg>
      <svg viewBox="0 0 12 12" aria-label="Social"><circle cx="6" cy="6" r="5" fill="#fff"/></svg>
    </div>

    <div class="wordmark">QUORVA</div>

    <div class="owner">
      <div class="owner-name">Name of Owner</div>
      <div class="owner-title">Founder And CEO</div>
    </div>

    <ul class="contact-list">
      <li>www.nameofcompany.com</li>
      <li>+1 (00) 000 00</li>
      <li>name@company.com</li>
      <li>nameofowner</li>
      <li>@nameofowner</li>
    </ul>
  </section>

</body>
</html>
```